Creating a Label for the Wine "Viña Aldaluz"

Viña Aldaluz
Viña Aldaluz means “lost mountain. Viña Aldaluz is a mountain far away from everything, lost in a wild place. The dimensios shoul be between 9cm x 11,5 cm and 12cm x 8 cm.

```html
<!DOCTYPE html>
<html lang="en">
<head>
<meta charset="utf-8">
<title>Viña Aldaluz – Wine Label</title>
<link rel="stylesheet" href="https://fonts.googleapis.com/css2?family=Cinzel:wght@400;600&family=Pinyon+Script&display=swap">
<style>
  :root {
    --page-bg: #ffffff;
    --paper-light: #f6efdc;
    --paper-mid: #ede2c6;
    --paper-edge: #e2d4b2;
    --gold-brown: #a3692c;
    --wine-red: #7b2b2c;
  }
  html, body {
    margin: 0;
    padding: 0;
    width: 1200px;
    height: 1039px;
    overflow: hidden;
    background: var(--page-bg);
  }
  .canvas {
    position: relative;
    width: 1200px;
    height: 1039px;
  }
  .label {
    position: absolute;
    left: 195px;
    top: 24px;
    width: 810px;
    height: 990px;
    background:
      radial-gradient(ellipse at 50% 45%, var(--paper-light) 0%, var(--paper-mid) 70%, var(--paper-edge) 100%);
    text-align: center;
  }
  .label > * {
    position: absolute;
    left: 0;
    right: 0;
    margin: 0;
  }
  .label__mark {
    top: 150px;
    left: 50%;
    right: auto;
    width: 120px;
    height: 120px;
    margin-left: -60px;
    border-radius: 50%;
    background: var(--gold-brown);
  }
  .label__winery {
    top: 335px;
    font-family: "Cinzel", serif;
    font-weight: 400;
    font-size: 56px;
    letter-spacing: 2px;
    color: var(--gold-brown);
  }
  .label__subtitle {
    top: 420px;
    font-family: "Cinzel", serif;
    font-weight: 400;
    font-size: 32px;
    letter-spacing: 3px;
    color: var(--gold-brown);
  }
  .label__wine {
    top: 575px;
    font-family: "Pinyon Script", cursive;
    font-size: 78px;
    line-height: 1;
    color: var(--wine-red);
  }
  .label__origin {
    top: 672px;
    font-family: "Cinzel", serif;
    font-weight: 400;
    font-size: 30px;
    letter-spacing: 4px;
    color: var(--wine-red);
  }
  .label__vintage {
    top: 858px;
    font-family: "Cinzel", serif;
    font-weight: 600;
    font-size: 28px;
    letter-spacing: 3px;
    color: var(--wine-red);
  }
</style>
</head>
<body>
  <main class="canvas">
    <section class="label">
      <div class="label__mark" aria-hidden="true"></div>
      <h1 class="label__winery">VINEYARD NAME</h1>
      <p class="label__subtitle">VINEYARDS</p>
      <h2 class="label__wine">Viña Aldaluz</h2>
      <p class="label__origin">ARAGON SPAIN</p>
      <p class="label__vintage">2010 | ESTATE GROWN</p>
    </section>
  </main>
</body>
</html>
```